Lead Sales Portal Needs to Generate B2B Signup's

We are looking for banner ad designs to drive new business (B2B) traffic to our insurance and mortgage industry self serve lead sites. The sites are HomeLoanProspectHub.com and PolicyBuyerHub.com, and we service over 45,000 insurance agents and mortgage lenders in a self serve lead portal model. We want our banners to generate more of these clients.

Our clients come to our sites, browse our database and then pick out and purchase the consumer leads that they need to generate new business.

We advertise extensively on Zyntrix and on other PPC platforms, and our existing banners are looking really tired.

Some of the ad copy that works well for us is:

Cherry Pick Your Life Leads - Why Pay More Than $3.50 For Life Insurance Leads?
Sign up today and we'll match up to $250

Agents - Here's $250 For New Clients. Cherry Pick Your Life Insurance Leads & Save! Sign up today and we'll match up to $250

One of our Landing Pages that performs well is here:
http://www.policybuyerhub.com/lp/008/

One of our competitors ad's are here:

http://www.brellow.com/search/results?q=QuoteMarten&ad=427360

We're looking for a design that is eye catching, uses our "Deeply Discounted Leads" and our "$250 match bonus"

This is the second contest that we have for the same sites. The previous designs were great and really performed well, so we are looking for new designs now that 6 months have passed. I have uploaded some winning banners from the last group for your information.

Reason: I've been asked by some of the designers to delay a day to get their designs in. I'm happy to do it!

Target Market(s)

These are insurance agents and mortgage lenders. All of our clients are business' or individuals within the business. This is a B2B campaign, so we need something that is professional and upscale. These are NOT consumer facing ad's!

Industry/Entity Type

Insurance

Font styles to use
Sans Serif

Requirements
Must have
• We must have the logos for the sites in the banners. Also, we must have a call to action arrow and "Go" button. Some animation is necessary, (especially around the arrow and the GO button).

One or two designs.

File type

.JPEG
.JPG
.PNG
.GIF

File size

150 KB or smaller

Image sizes

Vertical rectangle: 240 x 400
Mobile leaderboard: 320 x 50
Banner: 468 x 60
Leaderboard: 728 x 90
Square: 250 x 250
Small square: 200 x 200
Large rectangle: 336 x 280
Inline rectangle: 300 x 250
Skyscraper: 120 x 600
Wide skyscraper: 160 x 600
Half-page: 300 x 600
Large leaderboard: 970 x 90

```html
<!DOCTYPE html>
<html lang="en">
<head>
<meta charset="utf-8">
<title>Policy Buyer Hub – Banner Set</title>
<link rel="stylesheet" href="https://fonts.googleapis.com/css2?family=Open+Sans:wght@400&family=Roboto+Condensed:wght@400;700&display=swap">
<style>
  :root {
    --stage: #5c3120;
    --header-dark: #2f2f30;
    --panel-dark: #262627;
    --green-light: #a6cf1f;
    --green-dark: #5f8c0c;
    --photo-light: #eef3f7;
    --photo-mid: #c9d6e2;
    --headline-light: #e2e2e2;
    --headline-dark: #acacac;
    --headline-ink: #2a2a2a;
    --cta-light: #8a8a8a;
    --cta-dark: #5d5d5d;
    --button-top: #4a4a4a;
    --button-bottom: #141414;
    --white: #ffffff;
    --label: #ffffff;
  }
  * { margin: 0; padding: 0; box-sizing: border-box; }
  html, body { width: 1200px; height: 1000px; overflow: hidden; }
  body {
    background: var(--stage);
    position: relative;
    font-family: "Roboto Condensed", "Arial Narrow", sans-serif;
  }
  .banner {
    position: absolute;
    display: block;
    box-shadow: 0 6px 18px rgba(0,0,0,.55);
  }
  .banner--half-page { left: 199px; top: 60px; width: 390px; height: 780px; }
  .banner--vertical  { left: 689px; top: 320px; width: 312px; height: 520px; }
  .size-label {
    position: absolute;
    top: 868px;
    color: var(--label);
    font-family: "Roboto Condensed", "Arial Narrow", sans-serif;
    font-weight: 700;
    font-size: 64px;
    text-align: center;
    line-height: 1;
  }
  .size-label--half-page { left: 199px; width: 390px; }
  .size-label--vertical  { left: 689px; width: 312px; }

  .fill-header   { fill: var(--header-dark); }
  .fill-panel    { fill: var(--panel-dark); }
  .fill-white    { fill: var(--white); }
  .fill-green    { fill: var(--green-dark); }
  .stroke-green  { stroke: var(--green-light); fill: none; }
  .arrow-line    { stroke: var(--white); fill: none; stroke-width: 1.6; stroke-linecap: round; }
  .button-edge   { stroke: #9a9a9a; stroke-width: 1; }
  .stop-green-light { stop-color: var(--green-light); }
  .stop-green-dark  { stop-color: var(--green-dark); }
  .stop-photo-light { stop-color: var(--photo-light); }
  .stop-photo-mid   { stop-color: var(--photo-mid); }
  .stop-head-light  { stop-color: var(--headline-light); }
  .stop-head-dark   { stop-color: var(--headline-dark); }
  .stop-cta-light   { stop-color: var(--cta-light); }
  .stop-cta-dark    { stop-color: var(--cta-dark); }
  .stop-btn-top     { stop-color: var(--button-top); }
  .stop-btn-bottom  { stop-color: var(--button-bottom); }

  .brand-name { font-family: "Open Sans", Arial, sans-serif; font-weight: 400; fill: var(--white); }
  .headline   { font-family: "Roboto Condensed", "Arial Narrow", sans-serif; font-weight: 700; fill: var(--headline-ink); text-anchor: middle; }
  .benefit    { font-family: "Roboto Condensed", "Arial Narrow", sans-serif; font-weight: 400; fill: var(--white); }
  .cta-copy   { font-family: "Roboto Condensed", "Arial Narrow", sans-serif; font-weight: 400; fill: var(--white); }
  .cta-amount { font-weight: 700; }
  .go-label   { font-family: "Roboto Condensed", "Arial Narrow", sans-serif; font-weight: 700; fill: var(--white); }
</style>
</head>
<body>

<svg class="banner banner--half-page" viewBox="0 0 300 600" xmlns="http://www.w3.org/2000/svg">
  <defs>
    <linearGradient id="hp-green" x1="0" y1="0" x2="0" y2="1">
      <stop offset="0" class="stop-green-light"/><stop offset="1" class="stop-green-dark"/>
    </linearGradient>
    <linearGradient id="hp-photo" x1="0" y1="0" x2="1" y2="1">
      <stop offset="0" class="stop-photo-light"/><stop offset="1" class="stop-photo-mid"/>
    </linearGradient>
    <linearGradient id="hp-head" x1="0" y1="0" x2="0" y2="1">
      <stop offset="0" class="stop-head-light"/><stop offset="1" class="stop-head-dark"/>
    </linearGradient>
    <linearGradient id="hp-cta" x1="0" y1="0" x2="0" y2="1">
      <stop offset="0" class="stop-cta-light"/><stop offset="1" class="stop-cta-dark"/>
    </linearGradient>
    <linearGradient id="hp-btn" x1="0" y1="0" x2="0" y2="1">
      <stop offset="0" class="stop-btn-top"/><stop offset="1" class="stop-btn-bottom"/>
    </linearGradient>
  </defs>

  <rect class="photo" x="0" y="50" width="300" height="260" fill="url(#hp-photo)" role="img" aria-label="Photo of two smiling young insurance professionals in light blue shirts"/>
  <path class="header-band fill-header" d="M0,0 H300 V56 Q150,36 0,70 Z"/>
  <path class="swoosh-top" d="M0,70 Q150,36 300,56 V72 Q150,52 0,86 Z" fill="url(#hp-green)"/>
  <rect class="top-rule" x="0" y="0" width="300" height="1.5" fill="url(#hp-green)"/>

  <g class="brand">
    <circle class="fill-white" cx="77" cy="27" r="15"/>
    <text class="brand-name" x="97" y="34" font-size="20">Policy Buyer Hub</text>
  </g>

  <rect class="headline-panel" x="0" y="296" width="300" height="110" fill="url(#hp-head)"/>
  <path class="swoosh-bottom" d="M0,318 Q130,262 300,276 V298 Q150,286 0,332 Z" fill="url(#hp-green)"/>
  <text class="headline" x="150" y="350" font-size="21.5">WHY PAY MORE THAN $3.50</text>
  <text class="headline" x="150" y="379" font-size="21.5">FOR LIFE INSURANCE LEADS?</text>
  <rect class="headline-rule" x="0" y="402" width="300" height="5" fill="url(#hp-green)"/>

  <rect class="benefits-panel fill-panel" x="0" y="407" width="300" height="106"/>
  <g class="benefit-list">
    <circle class="fill-white" cx="40" cy="433" r="5"/>
    <text class="benefit" x="55" y="439" font-size="19">Chery Pick Your Leads</text>
    <circle class="fill-white" cx="40" cy="459" r="5"/>
    <text class="benefit" x="55" y="465" font-size="19">No Minimums</text>
    <circle class="fill-white" cx="40" cy="485" r="5"/>
    <text class="benefit" x="55" y="491" font-size="19">Deeply Discounted Leads</text>
  </g>

  <rect class="cta-panel" x="0" y="513" width="300" height="87" fill="url(#hp-cta)"/>
  <text class="cta-copy" x="13" y="548" font-size="20">Sign up today and we'll</text>
  <text class="cta-copy" x="13" y="578" font-size="20">match up to <tspan class="cta-amount" font-size="25">$250</tspan></text>
  <path class="arrow-line" d="M232,537 Q262,532 274,550"/>
  <path class="arrow-line" d="M268,549 L274,551 L275,544"/>

  <g class="go-button">
    <rect class="button-edge" x="208" y="559" width="82" height="33" rx="10" fill="url(#hp-btn)"/>
    <text class="go-label" x="223" y="583" font-size="19">GO</text>
    <path class="fill-green" d="M262,569 H272 V563 L285,575.5 L272,588 V582 H262 Z" fill="url(#hp-green)"/>
  </g>
</svg>

<svg class="banner banner--vertical" viewBox="0 0 240 400" xmlns="http://www.w3.org/2000/svg">
  <defs>
    <linearGradient id="vr-green" x1="0" y1="0" x2="0" y2="1">
      <stop offset="0" class="stop-green-light"/><stop offset="1" class="stop-green-dark"/>
    </linearGradient>
    <linearGradient id="vr-photo" x1="0" y1="0" x2="1" y2="1">
      <stop offset="0" class="stop-photo-light"/><stop offset="1" class="stop-photo-mid"/>
    </linearGradient>
    <linearGradient id="vr-head" x1="0" y1="0" x2="0" y2="1">
      <stop offset="0" class="stop-head-light"/><stop offset="1" class="stop-head-dark"/>
    </linearGradient>
    <linearGradient id="vr-cta" x1="0" y1="0" x2="0" y2="1">
      <stop offset="0" class="stop-cta-light"/><stop offset="1" class="stop-cta-dark"/>
    </linearGradient>
    <linearGradient id="vr-btn" x1="0" y1="0" x2="0" y2="1">
      <stop offset="0" class="stop-btn-top"/><stop offset="1" class="stop-btn-bottom"/>
    </linearGradient>
  </defs>

  <rect class="photo" x="0" y="45" width="240" height="170" fill="url(#vr-photo)" role="img" aria-label="Photo of two smiling young insurance professionals in light blue shirts"/>
  <path class="header-band fill-header" d="M0,0 H240 V50 Q120,34 0,62 Z"/>
  <path class="swoosh-top" d="M0,62 Q120,34 240,50 V63 Q120,47 0,75 Z" fill="url(#vr-green)"/>
  <rect class="top-rule" x="0" y="0" width="240" height="1.5" fill="url(#vr-green)"/>

  <g class="brand">
    <circle class="fill-white" cx="42" cy="24" r="14"/>
    <text class="brand-name" x="61" y="30" font-size="17.5">Policy Buyer Hub</text>
  </g>

  <rect class="headline-panel" x="0" y="205" width="240" height="68" fill="url(#vr-head)"/>
  <path class="swoosh-bottom" d="M0,222 Q110,180 240,192 V206 Q120,198 0,232 Z" fill="url(#vr-green)"/>
  <text class="headline" x="120" y="241" font-size="15.5">WHY PAY MORE THAN $3.50</text>
  <text class="headline" x="120" y="262" font-size="15.5">FOR LIFE INSURANCE LEADS?</text>
  <rect class="headline-rule" x="0" y="270" width="240" height="4" fill="url(#vr-green)"/>

  <rect class="benefits-panel fill-panel" x="0" y="274" width="240" height="66"/>
  <g class="benefit-list">
    <circle class="fill-white" cx="37" cy="288" r="3.8"/>
    <text class="benefit" x="48" y="292.5" font-size="14">Chery Pick Your Leads</text>
    <circle class="fill-white" cx="37" cy="306" r="3.8"/>
    <text class="benefit" x="48" y="310.5" font-size="14">No Minimums</text>
    <circle class="fill-white" cx="37" cy="325" r="3.8"/>
    <text class="benefit" x="48" y="329.5" font-size="14">Deeply Discounted Leads</text>
  </g>

  <rect class="cta-panel" x="0" y="340" width="240" height="60" fill="url(#vr-cta)"/>
  <text class="cta-copy" x="11" y="362" font-size="16">Sign up today and we'll</text>
  <text class="cta-copy" x="11" y="387" font-size="16">match up to <tspan class="cta-amount" font-size="20">$250</tspan></text>
  <path class="arrow-line" d="M186,352 Q215,347 226,362"/>
  <path class="arrow-line" d="M220,361 L226,363 L227,357"/>

  <g class="go-button">
    <rect class="button-edge" x="168" y="368" width="65" height="26" rx="8" fill="url(#vr-btn)"/>
    <text class="go-label" x="178" y="387" font-size="15">GO</text>
    <path d="M209,376 H217 V371 L227,381 L217,391 V386 H209 Z" fill="url(#vr-green)"/>
  </g>
</svg>

<div class="size-label size-label--half-page">300 x 600</div>
<div class="size-label size-label--vertical">240 x 400</div>

</body>
</html>
```